On-Hold Advertising & Music Business needs logo design

Our umbrella name is Brambleton Audio Collective. Our main focus is providing custom on hold advertising and music (plays to callers on hold and businesses all over North America and Canada) The name of the company under this umbrella name is (and has been for 30 years) Tidewell Soundworks. We pioneered the on hold marketing/advertising industry in the mid 80's. The final design should communicate CREATIVE ADVERTISING & MUSIC SPECIFIC TO THE ON HOLD APPLICATION. In addition to ON HOLD MUSIC AND MESSAGING, The company offers IN-BUILDING (OVERHEAD) MUSIC, DIGITAL SIGNAGE, AND access to PROFESSIONAL VOICE TALENT including MULTILINGUAL TALENT. The card can be (but doesn't have to be) double sided. I would like to see something on the front side that screams ADVERTISING FOR THE ON HOLD ENVIRONMENT, and then perhaps the balance of what we offer on the back side? We create an audio portrait of a busiiness through messages that play to the business' callers while on hold. I hjave included our current logo but I am open to new logo ideas if it doesn't fit well on a card.

Target Market(s)

Businesses of all kinds, shapes and sizes. Owners, Managers, Representatives from the companies

Industry/Entity Type

Advertising

Contact Information for Business Card

We want the front side to scream CREATIVE on hold advertising and music. it should feature our logo and have our contact information on it. It should also have room for names of staff (one per card of course along with their title)

Colors

Designer to choose colors to be used in the design.

Requirements
Must have
• Nameof the company and it should be clear what we are leading with: CREATIVE ON HOLD ADVERTISING AND MUSIC. It should at least list (okay on the back) our other services: In-Building (overhead) Music, Digital Signage and access to Professional Voice Talent for IVR/Telephone prompts (multi-language talent too)
Should not have
• The card should not be crammed with information (or at least not look like it is)

```html
<!DOCTYPE html>
<html lang="en">
<head>
<meta charset="utf-8">
<title>Brambleton Audio Collective – Business Card</title>
<link rel="stylesheet" href="https://fonts.googleapis.com/css2?family=Alegreya:wght@400&family=Open+Sans:wght@400;600&display=swap">
<style>
  :root {
    --stage: #1d1d1d;
    --paper: #ffffff;
    --brand-red: #e1202a;
    --ink: #2e3a42;
    --ink-soft: #3b3b3b;
    --cream: #fbeaea;
  }
  * { margin: 0; padding: 0; box-sizing: border-box; }
  html, body {
    width: 1200px; height: 900px; overflow: hidden;
    background: var(--stage);
  }
  .canvas { position: relative; width: 1200px; height: 900px; }

  .card {
    position: absolute; top: 170px;
    width: 347px; height: 561px;
  }
  .card--front { left: 259px; background: var(--paper); text-align: center; font-family: "Open Sans", Arial, sans-serif; color: var(--ink-soft); }
  .card--back { left: 631px; background: var(--brand-red); }

  .brand-mark {
    position: absolute; top: 92px; left: 0; width: 100%;
    display: flex; flex-direction: column; align-items: center; gap: 10px;
  }
  .brand-mark__dot {
    width: 64px; height: 64px; border-radius: 50%;
    background: var(--brand-red);
  }
  .brand-mark__name {
    font-weight: 600; font-size: 17px; letter-spacing: 1.5px;
    text-transform: uppercase; color: var(--ink); line-height: 1.35;
  }

  .staff {
    position: absolute; top: 333px; left: 0; width: 100%;
  }
  .staff__name { font-weight: 600; font-size: 21px; letter-spacing: 0.3px; color: var(--ink); line-height: 28px; }
  .staff__name .first { color: var(--brand-red); }
  .staff__title { font-size: 14.5px; line-height: 20px; }

  .contact {
    position: absolute; top: 393px; left: 0; width: 100%;
    list-style: none; font-size: 14.5px; line-height: 21px;
  }
  .contact__label { color: var(--brand-red); font-weight: 600; }
  .contact__web { color: var(--brand-red); }

  .address {
    position: absolute; top: 486px; left: 0; width: 100%;
    font-size: 14.5px; line-height: 18px; font-style: normal;
  }

  .services {
    position: absolute; top: 122px; left: 0; width: 100%;
    list-style: none; text-align: center;
    font-family: "Alegreya", Georgia, serif;
    font-size: 19.5px; letter-spacing: 0.6px; line-height: 35.8px;
    text-transform: uppercase; color: var(--cream);
  }
</style>
</head>
<body>
<main class="canvas">
  <section class="card card--front" aria-label="Card front">
    <div class="brand-mark">
      <span class="brand-mark__dot"></span>
      <p class="brand-mark__name">Brambleton Audio Collective<br>Tidewell Soundworks</p>
    </div>

    <div class="staff">
      <h1 class="staff__name"><span class="first">MAREN</span> HOLLOWAY</h1>
      <p class="staff__title">Managing Director</p>
    </div>

    <ul class="contact">
      <li><span class="contact__label">P:</span> 555-014-2270</li>
      <li><span class="contact__label">F:</span> 555-014-2270</li>
      <li><span class="contact__label">E:</span> hello@brambletonaudio.com</li>
      <li class="contact__web">www.brambletonaudio.com</li>
    </ul>

    <address class="address">48 Larkspur Lane, Suite 210<br>Hollisford, 40517</address>
  </section>

  <section class="card card--back" aria-label="Card back">
    <ul class="services">
      <li>On Hold Advertising</li>
      <li>Music On Hold</li>
      <li>In-Office Music</li>
      <li>In-Store Messaging</li>
      <li>IVR/Voice Prompts</li>
      <li>Digital Signage</li>
      <li>TV For Business</li>
      <li>Commercial Production</li>
      <li>Media Buying</li>
    </ul>
  </section>
</main>
</body>
</html>
```